Fernwood Chiropractic
letterhead/business cards
Project: Fernwood Chiropractic
Fernwood Chiropractic - Health
Creative Brief
Professional
Dr. Gavin P. Holcombe
Chiropractor
4817 Dunmore Road Building 2, Suite C-21 Philadelphia, PA 19144
drholcombe@fernwoodchiro-example.com
www.fernwoodchiro-example.com

```html
<!DOCTYPE html>
<html lang="en">
<head>
<meta charset="utf-8">
<title>Fernwood Chiropractic – Business Cards</title>
<link href="https://fonts.googleapis.com/css2?family=Cormorant+Garamond:wght@500&display=swap" rel="stylesheet">
<style>
  :root {
    --stage: #e6e8ea;
    --paper: #ffffff;
    --brand-blue: #1f5fa6;
    --brand-green: #4cae3c;
    --leaf-pale: #cfe8c6;
    --ink-white: #ffffff;
    --edge: #d3d6d9;
  }
  * { margin: 0; padding: 0; box-sizing: border-box; }
  html, body { width: 1200px; height: 991px; overflow: hidden; }
  body {
    background: var(--stage);
    font-family: "Cormorant Garamond", serif;
    font-weight: 500;
    position: relative;
  }
  .card {
    position: absolute;
    width: 580px;
    height: 330px;
    background: var(--paper);
    border-radius: 22px;
    overflow: hidden;
    box-shadow: 0 6px 0 var(--edge), 0 14px 30px rgba(0,0,0,0.18);
  }
  /* Front */
  .card-front { left: 560px; top: 110px; }
  .front-brand {
    position: absolute;
    left: 0; right: 0; top: 0; bottom: 0;
    display: flex; flex-direction: column; align-items: center; justify-content: center;
    gap: 22px;
  }
  .front-mark {
    width: 96px; height: 96px;
    border-radius: 50%;
    background: var(--leaf-pale);
  }
  .brand-name {
    color: var(--brand-blue);
    font-weight: 500;
    white-space: nowrap;
  }
  .front-brand .brand-name { font-size: 40px; }
  /* Back */
  .card-back { left: 60px; top: 520px; }
  .back-wave { position: absolute; inset: 0; }
  .back-brand {
    position: absolute;
    left: 0; right: 0; top: 40px;
    display: flex; align-items: center; justify-content: center; gap: 14px;
  }
  .back-brand-dot {
    width: 40px; height: 40px; border-radius: 50%;
    background: var(--leaf-pale);
  }
  .back-brand .brand-name { font-size: 30px; }
  .contact {
    position: absolute;
    color: var(--ink-white);
    font-size: 14px;
    line-height: 1.45;
    white-space: nowrap;
  }
  .contact-person { left: 28px; top: 196px; }
  .contact-person .person-name { font-size: 16px; }
  .contact-reach { right: 26px; top: 196px; text-align: right; }
  .social-row {
    position: absolute;
    left: 262px; top: 296px;
    display: flex; gap: 6px;
  }
  .social-dot { width: 11px; height: 11px; border-radius: 50%; background: var(--ink-white); }
</style>
</head>
<body>

  <section class="card card-front" aria-label="Business card front">
    <div class="front-brand">
      <div class="front-mark"></div>
      <div class="brand-name">Fernwood Chiropractic</div>
    </div>
  </section>

  <section class="card card-back" aria-label="Business card back">
    <svg class="back-wave" width="580" height="330" viewBox="0 0 580 330">
      <path d="M0 160 C150 110 330 200 580 130 L580 330 L0 330 Z" fill="var(--brand-green)"/>
      <path d="M0 150 C150 100 330 190 580 120" fill="none" stroke="var(--brand-blue)" stroke-width="5"/>
    </svg>

    <div class="back-brand">
      <div class="back-brand-dot"></div>
      <div class="brand-name">Fernwood Chiropractic</div>
    </div>

    <div class="contact contact-person">
      <div class="person-name">Dr. Gavin P. Holcombe</div>
      <div>Chiropractor</div>
      <div>4817 Dunmore Road Building 2,</div>
      <div>Suite C-21 Philadelphia, PA 19144</div>
    </div>

    <div class="social-row">
      <span class="social-dot"></span><span class="social-dot"></span><span class="social-dot"></span><span class="social-dot"></span>
    </div>

    <div class="contact contact-reach">
      <div>T (215) 555-0148</div>
      <div>F (215) 555-0193</div>
      <div>drholcombe@fernwoodchiro-example.com</div>
      <div>www.fernwoodchiro-example.com</div>
    </div>
  </section>

</body>
</html>
```